Business card for massage therapy company called Brook Fern Wellness

Need business card for massage therapy company called Brook Fern Wellness. Would like my logo on the front and the back of the card I have 3 options of logos and you can play with what looks better.

Would like this information displayed on the back of the card:

Marcus Ellery
Licensed Massage Therapist
321-555-0147
brookfern-example.com
brookfern_rest_

```html
<!DOCTYPE html>
<html lang="en">
<head>
<meta charset="utf-8">
<title>Brook Fern Wellness — Business Card</title>
<link rel="stylesheet" href="https://fonts.googleapis.com/css2?family=Marcellus&family=Lato:wght@400;700&display=swap">
<style>
  :root {
    --backdrop: #6a6a6a;
    --backdrop-dark: #555555;
    --sage: #6e7760;
    --sage-deep: #56603f;
    --copper: #c48d60;
    --cream: #f6efe9;
    --blush: #e8dbd0;
    --ivory: #fffdfb;
    --card-edge: #c9a27e;
  }
  * { box-sizing: border-box; margin: 0; padding: 0; }
  html, body { width: 1200px; height: 800px; overflow: hidden; }
  body {
    background: radial-gradient(ellipse at 50% 40%, var(--backdrop) 0%, var(--backdrop-dark) 100%);
    display: flex;
    align-items: center;
    justify-content: center;
    gap: 40px;
    font-family: "Lato", sans-serif;
  }
  .card {
    position: relative;
    width: 540px;
    height: 308px;
    border-radius: 4px;
    overflow: hidden;
    box-shadow: 0 0 0 2px var(--card-edge), 0 18px 30px rgba(0,0,0,0.35);
  }

  /* Front */
  .card-front { background: var(--sage); }
  .card-front .pattern-fill {
    position: absolute; inset: 0;
    background: linear-gradient(135deg, #737c65 0%, var(--sage) 50%, #687159 100%);
  }
  .front-brand {
    position: absolute; inset: 0;
    display: flex; align-items: center; justify-content: center; gap: 18px;
  }
  .brand-dot {
    width: 54px; height: 54px; border-radius: 50%;
    border: 1.5px solid var(--ivory);
  }
  .front-brand .brand-name {
    font-family: "Marcellus", serif;
    color: var(--ivory);
    font-size: 26px;
    letter-spacing: 3px;
    text-transform: uppercase;
    line-height: 1.25;
  }

  /* Back */
  .card-back .photo-fill {
    position: absolute; inset: 0;
    background: linear-gradient(120deg, var(--ivory) 0%, var(--cream) 40%, var(--blush) 75%, var(--cream) 100%);
  }
  .back-content {
    position: absolute; left: 34px; top: 38px; right: 34px; bottom: 30px;
  }
  .back-brand {
    font-family: "Marcellus", serif;
    color: var(--sage-deep);
    font-size: 30px;
    line-height: 1.1;
  }
  .person-name {
    margin-top: 34px;
    font-family: "Marcellus", serif;
    font-size: 27px;
    letter-spacing: 1.5px;
    color: var(--sage);
    text-transform: uppercase;
  }
  .person-title {
    font-family: "Lato", sans-serif;
    color: var(--copper);
    font-size: 15px;
    letter-spacing: 0.6px;
    margin-top: 2px;
  }
  .contact-list { list-style: none; margin-top: 12px; }
  .contact-list li {
    display: flex; align-items: center; gap: 10px;
    font-size: 15px; letter-spacing: 1px;
    color: var(--sage-deep);
    height: 24px;
  }
  .contact-icon { width: 14px; height: 14px; flex: none; }
  .mark-ring {
    position: absolute;
    right: 40px; top: 54px;
    width: 200px; height: 200px;
    border-radius: 50%;
    border: 3px solid var(--sage);
  }
</style>
</head>
<body>

  <section class="card card-front" aria-label="Card front">
    <div class="pattern-fill" role="img" aria-label="Tone-on-tone embossed repeat pattern in sage green"></div>
    <div class="front-brand">
      <span class="brand-dot"></span>
      <span class="brand-name">Brook Fern<br>Wellness</span>
    </div>
  </section>

  <section class="card card-back" aria-label="Card back">
    <div class="photo-fill" role="img" aria-label="Soft, faded photograph of a massage session in warm cream tones"></div>
    <div class="mark-ring"></div>
    <div class="back-content">
      <div class="back-brand">Brook Fern Wellness</div>
      <h1 class="person-name">Marcus Ellery</h1>
      <p class="person-title">Licensed Massage Therapist</p>
      <ul class="contact-list">
        <li>
          <svg class="contact-icon" viewBox="0 0 14 14" aria-hidden="true">
            <rect x="3.5" y="1" width="7" height="12" rx="1.2" fill="none" stroke="var(--copper)" stroke-width="1.2"/>
            <line x1="6" y1="11" x2="8" y2="11" stroke="var(--copper)" stroke-width="1.2"/>
          </svg>
          321-555-0147
        </li>
        <li>
          <svg class="contact-icon" viewBox="0 0 14 14" aria-hidden="true">
            <circle cx="7" cy="7" r="6" fill="none" stroke="var(--copper)" stroke-width="1.2"/>
            <ellipse cx="7" cy="7" rx="2.6" ry="6" fill="none" stroke="var(--copper)" stroke-width="1"/>
            <line x1="1" y1="7" x2="13" y2="7" stroke="var(--copper)" stroke-width="1"/>
          </svg>
          brookfern-example.com
        </li>
        <li>
          <svg class="contact-icon" viewBox="0 0 14 14" aria-hidden="true">
            <circle cx="7" cy="7" r="6" fill="var(--copper)"/>
          </svg>
          brookfern_rest_
        </li>
      </ul>
    </div>
  </section>

</body>
</html>
```